Konzert
Zielgruppe
Chor bzw. Vocalensemble
Aufgabenstellung
Konzertplakat - Handzettel
Titel: Die Wolkenbande gibt ein Mordskonzert
Ort: Tettnang im Lindenstube
Datum: 24.10.2015 20.00 Uhr
Es sollte auf jeden Fall erkennbar sein, dass es sich um ein Chorkonzert handelt.
Lieder sind alle zum Thema Verbrechen aber eher im zweideutigen Sinn.
Schon allein das Thema des Konzerts ist zweideutig zu verstehen.
Bei "Plinker Plonk" wird z.Bsp. eine Fliege in der Suppe gefunden...Ned Farrow wird einer erhängt, Mondscheinwalzr zwielichtige Barszene, bei der "Leisen Abreise" erleidet jemand einen Gedächnisverlust, River sings versinnbildlich Blättersterben (Herbst).
Wir könnten uns aber auch ein "retromäßiges" Plakat vorstellen, im Stil Gangsterzeit wie sie gut zum Mondscheinwalzer passt.
Wir werden Bilder anfügen, die eventuell auch nochmal überarbeitet werden müssen, weil sie ziemlich hell sind. Aber das können wir nach Auswahl noch machen. Die sind nicht zwingend einzusetzen, könnten aber mit eingebaut werden.
Wir sind offen für alles und sehr gespannt auf die Entwürfe.

```html
<!DOCTYPE html>
<html lang="de">
<head>
<meta charset="utf-8">
<title>Die Wolkenbande gibt ein Mordskonzert</title>
<link href="https://fonts.googleapis.com/css2?family=Special+Elite&display=swap" rel="stylesheet">
<style>
  :root {
    --bg: #000000;
    --ink-light: #ffffff;
    --crime-red: #b5121b;
    --label-white: #ffffff;
    --photo-light: #f1ddc9;
    --photo-mid: #d39a72;
    --photo-dark: #3a1d10;
    --badge-ring: #8a6a55;
    --badge-text: #f1ddc9;
  }
  html, body {
    margin: 0;
    padding: 0;
    overflow: hidden;
    background: var(--bg);
  }
  .poster {
    position: relative;
    width: 848px;
    height: 1200px;
    background: var(--bg);
    overflow: hidden;
    font-family: "Special Elite", "Courier New", monospace;
    color: var(--ink-light);
    text-transform: uppercase;
  }
  .abs { position: absolute; white-space: nowrap; margin: 0; }

  .headline-intro {
    left: 44px; top: 58px;
    font-size: 28px;
    letter-spacing: 9.5px;
  }

  .title {
    left: 146px; top: 104px;
    width: 652px;
    display: flex; gap: 3px;
    font-weight: normal;
  }
  .title-box {
    box-sizing: border-box;
    flex: 0 0 auto;
    overflow: hidden;
    background: var(--crime-red);
    height: 108px;
    display: flex; align-items: center; justify-content: space-evenly;
    font-size: 56px;
    color: var(--ink-light);
  }

  .date {
    left: 410px; top: 250px;
    font-size: 42px;
    letter-spacing: 12px;
    line-height: 1.25;
    transform: rotate(5deg);
    transform-origin: left top;
  }
  .date .time { display: block; padding-left: 6px; }
  .date .uhr { padding-left: 30px; }

  .tatort {
    left: 40px; top: 352px;
    font-size: 24px;
    letter-spacing: 0.3em;
    transform: rotate(-9deg);
    transform-origin: left top;
  }

  .tag {
    font-size: 24px;
    letter-spacing: 0.24em;
    padding: 8px 6px 8px 10px;
  }
  .tag-red { background: var(--crime-red); color: var(--ink-light); }
  .tag-white { background: var(--label-white); color: var(--crime-red); font-size: 28px; }

  .venue-town { left: 148px; top: 382px; transform: rotate(-8deg); transform-origin: left top; }
  .venue-im { left: 350px; top: 386px; transform: rotate(-6deg); transform-origin: left top; }
  .venue-hall { left: 236px; top: 440px; transform: rotate(-8deg); transform-origin: left top; }

  .claim-1 { left: 148px; top: 550px; transform: rotate(-9deg); transform-origin: left top; }
  .claim-2 { left: 370px; top: 502px; transform: rotate(-6deg); transform-origin: left top; }
  .claim-3 { left: 298px; top: 572px; transform: rotate(-9deg); transform-origin: left top; }
  .claim-4 { left: 594px; top: 586px; transform: rotate(-6deg); transform-origin: left top; }

  .choir-photo {
    left: 14px; top: 650px;
    width: 817px; height: 527px;
    border-radius: 42px;
    background:
      radial-gradient(ellipse 70% 65% at 50% 42%, var(--photo-light) 0%, var(--photo-mid) 45%, var(--photo-dark) 100%);
  }

  .badge-circle {
    left: 12px; top: 632px;
    width: 50px; height: 50px;
    border-radius: 50%;
    border: 3px solid var(--badge-ring);
  }
  .badge-name {
    left: 76px; top: 646px;
    font-size: 22px;
    letter-spacing: 0.2em;
    color: var(--badge-text);
  }
</style>
</head>
<body>
<main class="poster">
  <p class="abs headline-intro">Die Wolkenbande gibt ein</p>

  <h1 class="abs title">
    <span class="title-box" style="width:56px">M</span>
    <span class="title-box" style="width:157px"><span>O</span><span>R</span><span>D</span></span>
    <span class="title-box" style="width:159px"><span>S</span><span>K</span><span>O</span></span>
    <span class="title-box" style="width:159px"><span>N</span><span>Z</span><span>E</span></span>
    <span class="title-box" style="width:109px"><span>R</span><span>T</span></span>
  </h1>

  <p class="abs date">24.10.2015<span class="time">20.00 <span class="uhr">Uhr</span></span></p>

  <p class="abs tatort">Tatort:</p>
  <span class="abs tag tag-red venue-town">Tettnang</span>
  <span class="abs tag tag-red venue-im">im</span>
  <span class="abs tag tag-red venue-hall">Lindenstube</span>

  <span class="abs tag tag-white claim-1">Erleben</span>
  <span class="abs tag tag-white claim-2">Sie</span>
  <span class="abs tag tag-white claim-3">Atemberaubende</span>
  <span class="abs tag tag-white claim-4">Songs!</span>

  <div class="abs choir-photo" role="img" aria-label="Gruppenfoto des Chors in schwarzer Kleidung vor einer hellen Bühnenwand"></div>

  <span class="abs badge-circle" aria-hidden="true"></span>
  <p class="abs badge-name">Klangkreis</p>
</main>
</body>
</html>
```